Marketing Flyer for Wireless ISP

We are a Wireless ISP that has expanded its high speed business internet service to new area which has very poor internet. The new area is called Marlow Trade Estate.

We provide Highspeed, reliable and affordable business internet links.
We are competing against the cable and telephone companies to provide Internet over wireless links back to our fiber. Check out our news page www.vantorilink.com/news.aspx to watch a video about how the links are done. Might give you some ideas.

I need a reusable flyer that I can change the text on for future areas. It must be either 1 full page colour or 1/2 page color. It must also be in a format which I can email. I have photoshop and AI so changing a layer of text is easy.

Please include our web address, email and phone numbers as below. As well as our logo.

www.vantorilink.com
sales@vantorilink.com
555-284-7391

Target Market(s)

IT Managers or Small Business owners.

Industry/Entity Type

Telecommunications

Requirements
Must have
• I need a reusable flyer that I can change the text on for future areas. It must be either 1 full page colour or 1/2 page color. It must also be in a format which I can email. I have photoshop and AI so changing a layer of text is easy.
Nice to have
• something show faster speed than competitors balanced with reliability and affordable
Should not have
• provocative imaging.

```html
<!DOCTYPE html>
<html lang="en">
<head>
<meta charset="utf-8">
<title>Vantori Link – Business Internet Flyer</title>
<link rel="stylesheet" href="https://fonts.googleapis.com/css2?family=Lato:wght@400;700&family=Montserrat:wght@700;800&family=Oswald:wght@500;600&display=swap">
<style>
  :root {
    --stage: #e9e9e6;
    --ink: #0c0e11;
    --night: #121419;
    --sky: #1f9be0;
    --sky-deep: #1479bf;
    --sky-soft: #94dcfb;
    --signal-red: #e8173f;
    --paper: #ffffff;
    --mist: #d4d6d9;
    --slate: #2b2f36;
  }
  * { margin: 0; padding: 0; box-sizing: border-box; }
  html, body { width: 900px; height: 1200px; overflow: hidden; background: var(--stage); }
  .flyer {
    position: absolute; left: 30px; top: 12px;
    width: 700px; height: 980px;
    transform: scale(1.2); transform-origin: 0 0;
    background: var(--night); overflow: hidden;
    font-family: "Lato", sans-serif; color: var(--paper);
  }
  .hero-photo {
    position: absolute; left: 300px; top: 0; width: 400px; height: 375px;
    background: radial-gradient(ellipse at 60% 55%, #6f8ea6 0%, #34495a 40%, #151b22 80%);
  }
  .brand {
    position: absolute; left: 55px; top: 92px;
    display: flex; align-items: center; gap: 12px;
    font-family: "Lato", sans-serif; font-weight: 700; font-size: 30px; color: var(--sky);
  }
  .brand-dot { width: 22px; height: 22px; border-radius: 50%; background: var(--sky); }
  .shapes { position: absolute; left: 0; top: 0; }
  .headline { position: absolute; left: 22px; top: 383px; width: 295px; text-align: center; line-height: 1; }
  .headline .l1 { font-family: "Montserrat", sans-serif; font-weight: 700; font-size: 37px; color: var(--sky-soft); letter-spacing: 1px; }
  .headline .l2 { font-family: "Montserrat", sans-serif; font-weight: 800; font-size: 50px; margin-top: 8px; letter-spacing: 0.5px; }
  .headline .l3 { font-family: "Montserrat", sans-serif; font-weight: 800; font-size: 35px; color: var(--ink); margin-top: 8px; }
  .headline .l4 { font-family: "Oswald", sans-serif; font-weight: 500; font-size: 31px; margin-top: 10px; }
  .install { position: absolute; left: 0; top: 620px; width: 335px; height: 215px;
    background: linear-gradient(180deg, var(--mist) 0%, var(--paper) 35%, var(--paper) 70%, var(--mist) 100%); }
  .install-note { position: absolute; left: 30px; top: 34px; font-family: "Oswald", sans-serif; font-weight: 500; font-size: 27px; color: var(--slate); }
  .install-phone { position: absolute; left: 30px; top: 78px; display: flex; align-items: center; gap: 8px;
    font-family: "Oswald", sans-serif; font-weight: 600; font-size: 38px; color: var(--sky-deep); }
  .cost-box { position: absolute; left: 335px; top: 375px; width: 365px; height: 110px; background: var(--signal-red); }
  .cost-box p, .pitch p { font-size: 15.5px; line-height: 21px; text-align: justify; }
  .cost-box p { position: absolute; left: 48px; top: 12px; width: 282px; }
  .pitch { position: absolute; left: 335px; top: 485px; width: 365px; height: 335px; background: var(--ink); }
  .pitch p { position: absolute; left: 48px; top: 25px; width: 282px; }
  .ideal-title { position: absolute; left: 47px; top: 135px; font-weight: 700; font-size: 21px; color: var(--signal-red); }
  .ideal-list { position: absolute; left: 47px; top: 172px; list-style: none; font-size: 16.5px; line-height: 22px; }
  .ideal-list li::before { content: ""; display: inline-block; width: 5px; height: 5px; border-radius: 50%;
    background: var(--signal-red); margin-right: 8px; vertical-align: middle; }
  .footer { position: absolute; left: 0; top: 820px; width: 700px; height: 160px; }
  .contact { position: absolute; right: 30px; top: 46px; text-align: right; font-size: 27px; line-height: 37px; }
  .contact span { display: flex; align-items: center; justify-content: flex-end; gap: 12px; }
</style>
</head>
<body>
<div class="flyer">
  <div class="hero-photo" role="img" aria-label="Businessman in a suit holding glowing business graphs, a globe and devices in his open hands"></div>

  <div class="brand"><span class="brand-dot"></span>Vantori Link</div>

  <svg class="shapes" width="700" height="980" viewBox="0 0 700 980" aria-hidden="true">
    <defs>
      <linearGradient id="skyPanel" x1="0" y1="0" x2="0" y2="1">
        <stop offset="0" stop-color="#2fb0ee"/>
        <stop offset="1" stop-color="#1685cf"/>
      </linearGradient>
      <linearGradient id="skyBand" x1="0" y1="0" x2="1" y2="0">
        <stop offset="0" stop-color="#1a8fd9"/>
        <stop offset="1" stop-color="#2aa8ea"/>
      </linearGradient>
    </defs>
    <polygon points="0,175 335,375 335,700 0,700" fill="url(#skyPanel)"/>
    <line x1="0" y1="175" x2="335" y2="375" stroke="#ffffff" stroke-width="4"/>
    <rect x="0" y="820" width="700" height="160" fill="url(#skyBand)"/>
    <polygon points="0,858 335,825 700,825 700,832 335,836 0,872" fill="#ffffff"/>
  </svg>

  <div class="headline">
    <div class="l1">HIGHSPEED</div>
    <div class="l2">RELIABLE</div>
    <div class="l3">AFFORDABLE</div>
    <div class="l4">BUSINESS INTERNET LINKS</div>
  </div>

  <div class="install">
    <div class="install-note">48 hour install time available</div>
    <div class="install-phone">
      <svg width="28" height="28" viewBox="0 0 28 28" aria-hidden="true">
        <rect width="28" height="28" rx="5" fill="#1479bf"/>
        <path d="M9 6c1 0 2 3 2 4s-2 1-1.5 2.5 3 4 4.5 4.5 1.5-1.5 2.5-1.5 4 1 4 2-1 4-3 4C12 21 7 15 7 9c0-2 1-3 2-3z" fill="#fff"/>
      </svg>
      555-284-7391
    </div>
  </div>

  <div class="cost-box">
    <p>Cable and phone companies spendmillions digging trenches and running cables. These costs are passed on to you.</p>
  </div>

  <div class="pitch">
    <p>Wireless links are quickly deployed and tuneable, also wireless links can be turned up to provide faster speeds very easily!</p>
    <div class="ideal-title">Ideal For:</div>
    <ul class="ideal-list">
      <li>Busy office (15-30 users)</li>
      <li>Remote Cameras</li>
      <li>Video Conferencing</li>
      <li>Corporate Office VPN</li>
      <li>Remote Desktop</li>
      <li>Hosted Servers</li>
    </ul>
  </div>

  <div class="footer">
    <div class="contact">
      <span>www.vantorilink.com
        <svg width="24" height="24" viewBox="0 0 24 24" aria-hidden="true">
          <circle cx="12" cy="12" r="10" fill="none" stroke="#fff" stroke-width="2"/>
          <ellipse cx="12" cy="12" rx="4.5" ry="10" fill="none" stroke="#fff" stroke-width="1.6"/>
          <line x1="2" y1="12" x2="22" y2="12" stroke="#fff" stroke-width="1.6"/>
        </svg>
      </span>
      <span>sales@vantorilink.com
        <svg width="24" height="18" viewBox="0 0 24 18" aria-hidden="true">
          <rect x="1" y="1" width="22" height="16" fill="#fff"/>
          <polyline points="1,1 12,10 23,1" fill="none" stroke="#1a8fd9" stroke-width="1.6"/>
        </svg>
      </span>
    </div>
  </div>
</div>
</body>
</html>
```